Futuristic Trade Show Booth Design for Quorin Builders, Quorin Designers, and Quorin Corporate

We are seeking a cutting-edge and visually striking trade show booth design that showcases the synergy between our three brands: Quorin Designers (architectural design), Quorin Builders (construction services), and Quorin Corporate (unified identity). The design must reflect our commitment to innovation, professionalism, and forward-thinking solutions for commercial design and construction.

The booth will include three panels and two podiums, with a modern and futuristic aesthetic. The focus is on creating a cohesive yet distinctive identity for each brand while highlighting their integration under Quorin Corporate. Here’s what we envision:

Booth Specifications:
Backdrop Dimensions: Three panels of equal size.
Podiums: Two, one representing Quorin Designers and the other Quorin Builders.
Color Palette: Red (#D00E07), dark gray (#3B3838), light gray (#E0E0E0), and white (#FFFFFF).
Panel Breakdown:
1. Left Panel: Quorin Designers (Architectural Focus)

Content:
Taglines like “Design Smarter”
Highlight Quorin Designers’ architectural services : Commercial Architecture, Space Planning, Interior Design, Master Planning, 3D Renderings).
Visuals:
Include high-resolution 3D renderings of commercial spaces and modern blueprints.
Use a gradient background (dark gray to light gray) with overlays of translucent grids.
Icons representing architectural precision (e.g., drafting tools, rulers).
2. Center Panel: Quorin Corporate (Unified Identity)
Content:
Central tagline: “Intergrated Design-Build Solution”
Unified messaging emphasizing Quorin Corporate’s leadership in integrated design-build services.
Showcase how Quorin Designers and Quorin Builders collaborate seamlessly under Quorin Corporate.
Visuals:
A split image showing half blueprints (design) and half construction (build).
Gradient background transitioning from red to gray for continuity.
Icons or a flowchart highlighting the steps: “Concept > Design > Build > Completion.”
3. Right Panel: Quorin Builders (Construction Focus)

Content:
Taglines like “BUILD SMARTER
Highlight Quorin Builders’ construction services (Construction Management, Design-Build, General Contracting, Pre-Construction).
Visuals:

Overlay dynamic construction elements like cranes, scaffolding, and hard hats.
LED accents or subtle motion graphics to emphasize innovation.
Podium Design:
Quorin Designers Podium:
Gray-themed with the Quorin Designers logo and tagline: “DESIGN SMARTER”
Quorin Builders Podium:
Red-themed with the Quorin Builders logo and tagline: “BUILD SMARTER.”
Design Requirements:
Must reflect a modern and futuristic aesthetic.
Use clean, bold typography (e.g., Yantramanav or similar).
Ensure cohesive branding across all panels while keeping individual identities for Quorin Designers, Quorin Builders, and Quorin Corporate.
Balance professionalism with engaging visuals to attract visitors at the trade show.
Additional Notes:
The booth will serve as a centerpiece for showcasing Quorin Corporate’s integrated approach to commercial design and construction. The design must communicate trust, innovation, and expertise while captivating the audience at first glance.

Quorin Builders Website: www.quorinbuilders.example
Quorin Designers Website: www.quorindesigners.example
Quorin Corporate: www.quorincorporate.example
Logo Quorin Builders: https://files.example.net/share/a81kd92jfq0
Logo Quorin Designers: https://files.example.net/share/b27xm41pzr5
Logo Quorin Corporate: https://files.example.net/share/c63vn08twe2
The booth information and spec is on : https://www.standvelt.example/stand-ideas/linkline-10x10-stands/linkline-10x10-exhibit-stand-kit-c/

Target Market(s)

Commercial Property Developers, Corporate Real Estate Managers, Franchise Construction VP, Retail Franchise Owners,

Industry/Entity Type

Commercial Construction, Commercial Architecture

Font styles to use
Other font styles liked:
• Open to others but like Yantramanav, Poppins, Montserrat

Colors
EB3D1F
EC4F4E
F09395
F8D3D4
FCEDEE

Requirements
Must have
• Clear and prominent branding for Quorin Designers, Quorin Builders, and Quorin Corporate on their respective panels. Consistent color scheme using red (#D00E07), dark gray (#3B3838), light gray (#E0E0E0), and white (#FFFFFF) to unify the design. A modern and futuristic aesthetic that reflects innovation, precision, and professionalism. Distinct yet cohesive representation of services offered by Quorin Designers (architectural design), Quorin Builders (construction), and Quorin Corporate (integrated solutions).
Nice to have
• Subtle motion graphics or holographic overlays on panels to enhance the modern feel. A unified gradient background transitioning from red to gray to connect all panels visually. Visual flowcharts showing the step-by-step process of design-build services. Interactive design elements such as QR codes
Should not have
• Overly cluttered design that detracts from key messages or visuals. Fonts that are hard to read or do not match the modern and professional aesthetic. Excessive use of unrelated colors or mismatched visual styles. Misalignment or lack of clear separation between Quorin Designers, Quorin Builders, and Quorin Corporate branding.

```html
<!DOCTYPE html>
<html lang="en">
<head>
<meta charset="utf-8">
<title>Quorin Designers – Design Smarter Banner</title>
<link rel="stylesheet" href="https://fonts.googleapis.com/css2?family=Roboto:wght@500;700;900&display=swap">
<style>
  :root {
    --red: #d00e07;
    --dark-gray: #3b3838;
    --mid-gray: #555454;
    --light-gray: #e0e0e0;
    --soft-gray: #f1f1f1;
    --white: #ffffff;
    --ink: #2f2d2d;
  }
  * { margin: 0; padding: 0; box-sizing: border-box; }
  html, body {
    width: 1200px; height: 2560px; overflow: hidden;
    background: var(--white);
    font-family: "Roboto", Arial, sans-serif;
  }
  .banner { position: relative; width: 1200px; height: 2560px; overflow: hidden; }
  .banner-shapes { position: absolute; inset: 0; }

  .brand {
    position: absolute; left: 0; top: 126px; width: 1200px;
    display: flex; flex-direction: column; align-items: center; gap: 30px;
  }
  .brand-mark { width: 120px; height: 120px; background: var(--red); }
  .brand-name {
    font-weight: 500; font-size: 30px; line-height: 36px; letter-spacing: 10px;
    color: var(--ink); text-transform: uppercase;
  }

  .headline {
    position: absolute; left: 66px; top: 653px; width: 1068px; height: 200px;
    display: flex; align-items: center; justify-content: center;
    color: var(--white); font-weight: 700; font-size: 118px; letter-spacing: 1px;
  }

  .service {
    position: absolute; display: flex; align-items: center; gap: 20px;
  }
  .service-icon {
    width: 150px; height: 150px; border-radius: 50%;
    background: var(--soft-gray);
    display: flex; align-items: center; justify-content: center; flex: none;
  }
  .service-icon svg { width: 96px; height: 96px; }
  .service-label {
    font-weight: 500; font-size: 41px; line-height: 56px; color: var(--ink);
  }
  .service--commercial { left: 181px; top: 899px; }
  .service--space      { left: 691px; top: 904px; }
  .service--interior   { left: 181px; top: 1088px; }
  .service--master     { left: 691px; top: 1088px; }
  .service--rendering  { left: 411px; top: 1251px; }
</style>
</head>
<body>
<main class="banner">
  <svg class="banner-shapes" viewBox="0 0 1200 2560" xmlns="http://www.w3.org/2000/svg">
    <defs>
      <linearGradient id="backdrop-gradient" x1="0" y1="0" x2="0" y2="1">
        <stop offset="0" stop-color="#4c4b4b"/>
        <stop offset="0.22" stop-color="#5b5a5a"/>
        <stop offset="0.55" stop-color="#b9b9b9"/>
        <stop offset="0.75" stop-color="#e6e6e6"/>
        <stop offset="1" stop-color="#f4f4f4"/>
      </linearGradient>
      <linearGradient id="lobby-gradient" x1="0" y1="0" x2="0" y2="1">
        <stop offset="0" stop-color="#8e8e8e"/>
        <stop offset="0.35" stop-color="#d9d9d9"/>
        <stop offset="0.7" stop-color="#bdbdbd"/>
        <stop offset="1" stop-color="#9a9494"/>
      </linearGradient>
    </defs>

    <!-- backdrop -->
    <rect width="1200" height="2560" fill="url(#backdrop-gradient)"/>

    <!-- blueprint areas -->
    <rect role="img" aria-label="Faint architectural floor plan drawing" x="0" y="330" width="420" height="260" fill="#ffffff" opacity="0.08"/>
    <rect role="img" aria-label="Faint architectural blueprint with grid lines" x="700" y="1330" width="500" height="440" fill="#ffffff" opacity="0.18"/>

    <!-- header -->
    <polygon points="0,0 1200,0 1200,288 600,470 0,288" fill="var(--white)"/>
    <rect x="0" y="0" width="1200" height="14" fill="var(--red)"/>
    <polygon points="390,14 810,14 600,74" fill="var(--dark-gray)"/>
    <polygon points="0,288 600,470 1200,288 1200,314 600,496 0,314" fill="var(--red)"/>
    <polygon points="0,314 600,496 1200,314 1200,322 600,504 0,322" fill="var(--white)"/>
    <polygon points="0,322 600,504 1200,322 1200,332 600,514 0,332" fill="var(--red)"/>

    <!-- services area -->
    <polygon points="0,1270 1200,1270 1200,1320 600,1500 0,1320" fill="var(--red)"/>
    <polygon points="0,1270 1200,1270 1200,1304 600,1478 0,1304" fill="var(--white)"/>
    <polygon points="0,1270 1200,1270 1200,1296 600,1468 0,1296" fill="var(--red)"/>
    <polygon points="0,880 1200,880 1200,1286 600,1456 0,1286" fill="var(--white)"/>
    <polygon points="0,868 66,853 1134,853 1200,868 1200,882 0,882" fill="var(--red)"/>

    <!-- headline box -->
    <rect x="66" y="653" width="1068" height="200" fill="var(--red)"/>
    <rect x="76" y="663" width="1048" height="180" fill="none" stroke="var(--white)" stroke-width="3"/>

    <!-- lobby visual frame -->
    <polygon points="0,1790 600,1600 1200,1790 1200,2560 0,2560" fill="var(--white)"/>
    <polygon role="img" aria-label="3D rendering of a modern commercial lobby with elevator, reception desk and red lounge chair"
      points="0,1830 330,1712 870,1712 1200,1830 1200,2390 870,2450 330,2450 0,2390" fill="url(#lobby-gradient)"/>
    <polygon points="350,1700 850,1700 600,1625" fill="var(--red)"/>
    <polygon points="350,2470 850,2470 600,2545" fill="var(--red)"/>
  </svg>

  <header class="brand">
    <div class="brand-mark"></div>
    <div class="brand-name">Quorin Designers</div>
  </header>

  <h1 class="headline">DESIGN SMARTER</h1>

  <div class="service service--commercial">
    <div class="service-icon">
      <svg viewBox="0 0 96 96" fill="none" stroke="#d00e07" stroke-width="3" stroke-linejoin="round">
        <rect x="12" y="20" width="66" height="60" rx="4"/>
        <polygon points="22,70 22,38 54,70"/>
        <line x1="40" y1="58" x2="76" y2="14"/>
        <line x1="48" y1="64" x2="84" y2="20"/>
        <line x1="76" y1="14" x2="84" y2="20"/>
      </svg>
    </div>
    <div class="service-label">Commercial<br>Architecture</div>
  </div>

  <div class="service service--space">
    <div class="service-icon">
      <svg viewBox="0 0 96 96" fill="none" stroke="#d00e07" stroke-width="3">
        <rect x="34" y="34" width="28" height="28"/>
        <line x1="48" y1="8" x2="48" y2="88"/>
        <line x1="8" y1="48" x2="88" y2="48"/>
        <line x1="34" y1="14" x2="34" y2="82" stroke-dasharray="4 4"/>
        <line x1="62" y1="14" x2="62" y2="82" stroke-dasharray="4 4"/>
      </svg>
    </div>
    <div class="service-label">Space<br>Planning</div>
  </div>

  <div class="service service--interior">
    <div class="service-icon">
      <svg viewBox="0 0 96 96" fill="none" stroke="#d00e07" stroke-width="3">
        <rect x="12" y="12" width="72" height="72"/>
        <line x1="40" y1="12" x2="40" y2="34"/>
        <line x1="40" y1="48" x2="40" y2="84"/>
        <line x1="12" y1="48" x2="40" y2="48"/>
        <line x1="56" y1="12" x2="56" y2="40"/>
        <line x1="56" y1="40" x2="84" y2="40"/>
        <line x1="56" y1="62" x2="84" y2="62"/>
      </svg>
    </div>
    <div class="service-label">Interior<br>Design</div>
  </div>

  <div class="service service--master">
    <div class="service-icon">
      <svg viewBox="0 0 96 96" fill="none" stroke="#d00e07" stroke-width="3">
        <rect x="10" y="30" width="76" height="50" rx="14"/>
        <rect x="42" y="10" width="12" height="62"/>
        <circle cx="26" cy="55" r="7"/>
        <circle cx="70" cy="55" r="7"/>
        <line x1="36" y1="42" x2="60" y2="42"/>
      </svg>
    </div>
    <div class="service-label">Master<br>Planning</div>
  </div>

  <div class="service service--rendering">
    <div class="service-icon">
      <svg viewBox="0 0 96 96" fill="none" stroke="#d00e07" stroke-width="3" stroke-linejoin="round">
        <polygon points="48,10 84,28 84,68 48,86 12,68 12,28"/>
        <polyline points="12,28 48,46 84,28"/>
        <line x1="48" y1="46" x2="48" y2="86"/>
      </svg>
    </div>
    <div class="service-label">3D Rendering</div>
  </div>
</main>
</body>
</html>
```